Elegant eBook Word Template Design Required

I need an ebook template designed to match my website branding. It needs to include index, intro, chapters and about me. Word format required.

I will be using this template to create downloadable pdfs on my website.

For branding visit my website http://ravelkostin.com.au

Facebook: @RavelKostinOnline

Target Market(s)

Business owners, Entrepreneurs

Industry/Entity Type

Business Consultant

Font styles to use
Other font styles liked:
• check website

Colors

Designer to choose colors to be used in the design.

Requirements
Must have
• - Font and colour scheme must match my website branding

```html
<!DOCTYPE html>
<html lang="en">
<head>
<meta charset="utf-8">
<title>Ravel Kostin eBook Template</title>
<link rel="stylesheet" href="https://fonts.googleapis.com/css2?family=Montserrat:wght@400;500;600;700&display=swap">
<style>
  :root {
    --canvas-bg: #e4e6e8;
    --page-bg: #ffffff;
    --brand-blue: #3d95c9;
    --ink: #1f1f1f;
    --ink-soft: #3a3a3a;
    --heading-dark: #2b2b2b;
    --photo-dark: #3b3f46;
    --photo-light: #9aa0a8;
  }
  * { box-sizing: border-box; margin: 0; padding: 0; }
  html, body {
    width: 1200px; height: 2474px; overflow: hidden;
    background: var(--canvas-bg);
    font-family: "Montserrat", Arial, sans-serif;
    color: var(--ink);
  }
  .spread {
    width: 1200px; height: 2474px;
    padding-top: 40px;
    display: flex; flex-direction: column; align-items: center; gap: 74px;
  }
  .page {
    width: 880px; height: 1160px;
    background: var(--page-bg);
    position: relative; overflow: hidden;
    padding: 40px 100px 0;
  }
  .brand {
    display: flex; flex-direction: column; align-items: center; gap: 10px;
  }
  .brand-mark {
    width: 58px; height: 58px; border-radius: 50%;
    background: var(--brand-blue);
  }
  .brand-name {
    font-weight: 700; font-size: 27px; letter-spacing: 0.5px;
    color: var(--ink); text-transform: uppercase;
  }
  .feature {
    margin-top: 130px;
    display: flex; gap: 10px; height: 240px;
  }
  .video {
    width: 300px; height: 240px; position: relative;
    background: linear-gradient(135deg, var(--photo-light), var(--photo-dark));
  }
  .video-play { position: absolute; right: 16px; bottom: 16px; }
  .quote {
    flex: 1; background: var(--brand-blue); color: #fff;
    padding: 20px 22px; font-size: 16px; line-height: 1.3; font-weight: 500;
  }
  .quote p + p { margin-top: 22px; }
  .quote cite { display: block; font-style: normal; font-size: 11px; margin-top: 4px; }
  .body-copy { margin-top: 14px; font-size: 14.5px; line-height: 1.3; color: var(--ink-soft); font-weight: 500; }
  .body-copy p + p { margin-top: 14px; }
  .body-copy .callout { font-weight: 700; color: var(--ink); }
  .section-title {
    position: absolute; left: 100px; top: 1055px;
    font-size: 50px; font-weight: 700; color: var(--heading-dark); letter-spacing: 1px;
  }
  .lorem { margin-top: 95px; font-size: 14.5px; line-height: 1.28; color: var(--ink-soft); }
  .lorem p + p { margin-top: 16px; }
  .chapter-title {
    position: absolute; left: 100px; top: 1062px;
    font-size: 36px; font-weight: 700; color: var(--brand-blue); letter-spacing: 1px;
  }
</style>
</head>
<body>
<main class="spread">

  <section class="page page-about">
    <header class="brand">
      <span class="brand-mark"></span>
      <span class="brand-name">Ravel Kostin</span>
    </header>

    <div class="feature">
      <div class="video" role="img" aria-label="Video still of the author in a dark suit smiling">
        <svg class="video-play" width="58" height="58" viewBox="0 0 58 58" aria-hidden="true">
          <circle cx="29" cy="29" r="29" fill="#ffffff"/>
          <path d="M22 16 L44 29 L22 42 Z" fill="#2b2b2b"/>
        </svg>
      </div>
      <blockquote class="quote">
        <p>"There is a beautiful part of us, a deeper part of us, that when we get in tune with, we can grow beyond tough circumstances.</p>
        <p>It's like a lotus that glows beautifully and floats in a dirty pond"</p>
        <cite>– Ravel Kostin</cite>
      </blockquote>
    </div>

    <div class="body-copy">
      <p>I grew up in a challenged, poor neighbourhood in Mumbai.<br>There, myself and 13 others all lived in a single bedroom on the fifth floor of an old dingy apartment. It was a bedroom that wouldn't be any larger than a western kitchen.</p>
      <p>So I'm humbled to have experienced limitations of life. I know what it's like. And more importantly, I know it is not the be all and end all.</p>
      <p>In fact, it was far from it. You see, no matter how tough it seemed, each day, from the fifth storey of our apartment, I saw below us, the real slums of Mumbai. There, people were living with no shelter, no food, no water, and certainly no toilets.</p>
      <p>If you think you are on the bottom rung, look around you and you'll see that there are lessons to be learned about.</p>
      <p>So I realized I actually had it pretty good.</p>
      <p>When I decided to be grateful for what I had, things just fell in place. I took opportunities as they came, worked hard, got scholarships, and before I knew it... I was being sent off to America for a Master's degree in engineering!</p>
      <p>Things just kept getting better.</p>
      <p>I graduated with honours, got myself a Master's degree, published many papers and presentations in the field of engineering and IT technology, and ended up with a high paying job even in an economic downturn!</p>
      <p class="callout">Being Grateful for What I Had, Gave Me Access to More Opportunities!</p>
      <p>What are you grateful for today?</p>
    </div>

    <h2 class="section-title">ABOUT ME</h2>
  </section>

  <section class="page page-chapter">
    <header class="brand">
      <span class="brand-mark"></span>
      <span class="brand-name">Ravel Kostin</span>
    </header>

    <div class="lorem">
      <p>Lorem ipsum dolor sit amet, consectetur adipiscing elit. Quisque ultrices, ante vel euismod mattis, felis sem Lorem ipsum dolor sit amet, consectetur adipiscing elit. Quisque ultrices, ante vel euismod mattis, felis sem Lorem ipsum dolor sit amet, consectetur adipiscing elit.</p>
      <p>Lorem ipsum dolor sit amet, consectetur adipiscing elit. Quisque ultrices, ante vel euismod mattis, felis sem Lorem ipsum dolor sit amet, consectetur adipiscing elit. Quisque ultrices, ante vel euismod mattis, felis sem Lorem ipsum dolor sit amet, consectetur adipiscing elit. Quisque ultrices, ante vel euismod mattis, felis sem Lorem ipsum dolor sit amet, consectetur adipiscing elit. Quisque ultrices, ante vel euismod mattis, felis sem Lorem ipsum dolor sit amet, consectetur adipiscing elit.</p>
      <p>Lorem ipsum dolor sit amet, consectetur adipiscing elit. Quisque ultrices, ante vel euismod mattis, felis sem Lorem ipsum dolor sit amet, consectetur adipiscing elit. Quisque ultrices, ante vel euismod mattis, felis sem Lorem ipsum dolor sit amet, consectetur adipiscing elit. Quisque ultrices, ante vel euismod mattis, felis sem Lorem ipsum dolor sit amet, consectetur adipiscing elit. Quisque ultrices, ante vel euismod mattis, felis sem Lorem ipsum dolor sit amet, consectetur adipiscing elit. Quisque ultrices, ante vel euismod mattis, felis sem Lorem ipsum dolor sit amet, consectetur adipiscing elit. Quisque ultrices, ante vel euismod mattis, felis sem Lorem ipsum dolor sit amet, consectetur adipiscing elit.</p>
      <p>Lorem ipsum dolor sit amet, consectetur adipiscing elit. Quisque ultrices, ante vel euismod mattis, felis sem Lorem ipsum dolor sit amet, consectetur adipiscing elit. Quisque ultrices, ante vel euismod mattis, felis sem Lorem ipsum dolor sit amet, consectetur adipiscing elit. Quisque ultrices, ante vel euismod mattis, felis sem Lorem ipsum dolor sit amet, consectetur adipiscing elit. Quisque ultrices, ante vel euismod mattis, felis sem Lorem ipsum dolor sit amet, consectetur adipiscing elit. Quisque ultrices, ante vel euismod mattis, felis sem Lorem ipsum dolor sit amet.</p>
      <p>Lorem ipsum dolor sit amet, consectetur adipiscing elit. Quisque ultrices, ante vel euismod mattis, felis sem Lorem ipsum dolor sit amet, consectetur adipiscing elit. Quisque ultrices, ante vel euismod mattis, felis sem Lorem ipsum dolor sit amet, consectetur adipiscing elit.</p>
      <p>Lorem ipsum dolor sit amet, consectetur adipiscing elit. Quisque ultrices, ante vel euismod mattis, felis sem Lorem ipsum dolor sit amet, consectetur adipiscing elit. Quisque ultrices, ante vel euismod mattis, felis sem Lorem ipsum dolor sit amet, consectetur adipiscing elit.</p>
    </div>

    <h2 class="chapter-title">CHAPTER 1</h2>
  </section>

</main>
</body>
</html>
```